Etiketten für Gin
Zielgruppe
Unser Firma ist Errichter für Sicherheitstechnik und hat letztes Jahr einen eigenen Gin entwickelt und Ihn unter dem Namen Nachtfalke an Kunden verschenkt und ein paar Märkte zur Probe damit ausgestattet.
Aufgabenstellung
Das derzeitige Design ist schon nicht schlecht aber wurde von uns selber entwickelt und soll nun professionell Designt und Marktfähig für WOLNA und Co gemacht werden. Es soll eine White und Black Edition geben, die beiden unterscheiden sich im Geschmack und haben entweder Silber oder Gold Flakes mit drin. Daher muss das eine Etikett im Backround Weiß und das ander Schwarz sein.
Wichtig !! Der Totenkopf muss für beide Flaschen bleiben, der bestehende Totenkopf ist nicht in Beton gemeißelt, daher macht uns coole kreative Vorschläge.

```html
<!DOCTYPE html>
<html lang="de">
<head>
<meta charset="utf-8">
<title>Nachtfalke Gin – White &amp; Black Edition</title>
<link href="https://fonts.googleapis.com/css2?family=Alfa+Slab+One&family=Roboto+Slab:wght@700&display=swap" rel="stylesheet">
<style>
  :root {
    --stage: #eceded;
    --paper-white: #ffffff;
    --paper-black: #050505;
    --ink-black: #111111;
    --ink-white: #f2f2f2;
    --accent-red: #d0262c;
    --art-light-a: #e4e4e4;
    --art-light-b: #9a9a9a;
    --art-dark-a: #5a5a5a;
    --art-dark-b: #1c1c1c;
  }
  * { margin: 0; padding: 0; box-sizing: border-box; }
  html, body { width: 905px; height: 1200px; overflow: hidden; }
  body { background: var(--stage); position: relative; }

  .label {
    position: absolute;
    top: 402px;
    width: 372px;
    height: 396px;
    box-shadow: 0 2px 10px rgba(0,0,0,0.12);
  }
  .label--white { left: 52px; background: var(--paper-white); color: var(--ink-black); }
  .label--black { left: 494px; background: var(--paper-black); color: var(--ink-white); }

  .label__art {
    position: absolute;
    left: 40px;
    top: 42px;
    width: 292px;
    height: 212px;
    border-radius: 40% 40% 45% 45%;
  }
  .label--white .label__art { background: radial-gradient(ellipse at center, var(--art-light-b) 0%, var(--art-light-a) 70%, var(--paper-white) 100%); }
  .label--black .label__art { background: radial-gradient(ellipse at center, var(--art-dark-a) 0%, var(--art-dark-b) 70%, var(--paper-black) 100%); }

  .label__text {
    position: absolute;
    left: 0;
    right: 0;
    top: 266px;
    height: 112px;
    display: flex;
    justify-content: center;
    align-items: center;
    gap: 12px;
  }
  .label__type {
    writing-mode: vertical-rl;
    transform: rotate(180deg);
    font-family: "Roboto Slab", serif;
    font-weight: 700;
    font-size: 12px;
    letter-spacing: 0.5px;
    color: var(--accent-red);
  }
  .label__name {
    font-family: "Alfa Slab One", serif;
    font-size: 40px;
    line-height: 1.2;
    letter-spacing: 1px;
    text-align: center;
  }
  .label__volume {
    writing-mode: vertical-rl;
    font-family: "Roboto Slab", serif;
    font-weight: 700;
    font-size: 20px;
    line-height: 1;
    color: var(--accent-red);
    letter-spacing: 1px;
  }
  .label__volume small { font-size: 8px; letter-spacing: 0.5px; margin: 5px 0; }
</style>
</head>
<body>
  <section class="label label--white">
    <div class="label__art" role="img" aria-label="Illustration: Totenkopf mit Mütze und Augenmaske vor zwei gekreuzten Brechstangen"></div>
    <div class="label__text">
      <span class="label__type">HANDMADE GIN</span>
      <div class="label__name">NACHT<br>FALKE</div>
      <span class="label__volume">0,5 <small>LITER</small> 40%</span>
    </div>
  </section>

  <section class="label label--black">
    <div class="label__art" role="img" aria-label="Illustration: Totenkopf mit Mütze und Augenmaske vor zwei gekreuzten Brechstangen, hell auf Schwarz"></div>
    <div class="label__text">
      <span class="label__type">HANDMADE GIN</span>
      <div class="label__name">NACHT<br>FALKE</div>
      <span class="label__volume">0,5 <small>LITER</small> 40%</span>
    </div>
  </section>
</body>
</html>
```